Leading Restaurant Website Redesign (Home Page + 1)

I need an updated home page design for a leading regional restaurant website - Marlo.

Marlo is a well established restaurant in Kestra, Queensland, Australia. Kestra is a well known holiday destination but also has a thriving residential population who love dining out.

The restaurant overlooks the Kestra River and has terraces overlooking the river views to enjoy the warm summers and relatively mild winters in Queensland.

The owner of Marlo has a French heritage. Food is delicious but not pretentious and the atmosphere at Marlo is fun and congenial (not stuffy). The food is delicious and the owner is passionate about the meal designs and his wine cellar. The restaurant would sit somewhere between European bistro and fine dining.
Marlo has an enviable wine list - and the owner and wine manager host regular events showcasing Australia wine makers and their cellar releases.

The main goal of the website is to let visitors know about the hours, various meal specials, options for groups and functions, and other relevant information.

The existing website has not been changed for some time. It is available at https://marlobayfront.com.au.

For the website refresh, we are looking for a new Home page design (including header and footer) and a design for the Groups and Function page (see attached document for sections/content).

The design should position Marlo as a premium destination but should prioritise clarity of information and come off as 'classy but welcoming'. The primary colour of the site should remain similar to the current site. However, feel free to design a suitable colour palette to ensure primary and secondary calls to action are highly visible provided the brand 'feel' remains consistent with the current colour scheme etc.

The design MUST include considerations for responsive design from mobile to desktop viewports. We suggest a max page width of 1366px for desktop. The web builder can cater for numberically scaled spacing and font sizes.

We'll be building on WordPress using BricksBuilder, Automatic CSS, and Frames:
https://plankwright.io/
https://tidystyler.com/
https://usepanels.io/

There is a library of standard Frames sections and components layouts that may be used if desired as a basis:
https://usepanels.io/panels/

FONTS
The logo font is currently Twang.
Heading fonts may also use this font if this suits the design. Otherwise, suggest something from Google or free font libraries that will create a similar fun and informal feel while remaining a little stylish.
Site currently uses Nunito as the body font. Happy to stick with this unless you have another suggestion.

See the attached document for the content and order of sections for the two pages.

Target Market(s)

Local diners, holiday makers, interstate visitors searching for a great place to eat

Industry/Entity Type

Restaurant

Number of Pages Required

2 page

Font styles to use
Sans Serif
Other font styles liked:
• See description and current website

Colors
0054AA
0677BA
7BADD7
CADEEF
E8F1F8

Requirements
Must have
• Layout designs for the provided content sections for 2 pages.
Nice to have
• An elegant splash/hero section that positions the restaurant as welcoming but sophisticated

```html
<!DOCTYPE html>
<html lang="en">
<head>
<meta charset="utf-8">
<title>Marlo Kestra – Home</title>
<link href="https://fonts.googleapis.com/css2?family=Caveat+Brush&family=Nunito:wght@400;600;700;800&display=swap" rel="stylesheet">
<style>
:root{
  --blue:#0054AA;
  --blue-mid:#0677BA;
  --blue-soft:#7BADD7;
  --blue-pale:#CADEEF;
  --blue-mist:#E8F1F8;
  --red:#c0392b;
  --yellow:#f2d230;
  --ink:#1d2430;
  --muted:#5b6675;
  --white:#ffffff;
  --black:#0d0d0d;
}
*{box-sizing:border-box;margin:0;padding:0}
html,body{width:1200px;height:4536px;overflow:hidden}
body{font-family:"Nunito",sans-serif;color:var(--ink);background:var(--white);position:relative}
section,header,footer{position:relative;width:1200px;overflow:hidden}
.ph{position:absolute;display:block}
.title{font-family:"Caveat Brush",cursive;font-size:48px;text-align:center;line-height:1;font-weight:400}
.btn{display:inline-block;font-size:13px;font-weight:700;padding:8px 22px;border-radius:3px;text-decoration:none;white-space:nowrap}
.btn-solid{background:var(--blue);color:var(--white)}
.btn-outline{border:1.5px solid currentColor;color:var(--white)}
.btn-outline-blue{border:1.5px solid var(--blue);color:var(--blue);background:var(--white)}

/* hero */
.hero{height:580px;background:#2a2320}
.hero .ph{inset:0;background:radial-gradient(ellipse at 45% 40%,#8a6a55 0%,#4c3a30 45%,#1e1814 100%)}
.hero::after{content:"";position:absolute;inset:0;background:linear-gradient(180deg,rgba(0,0,0,.35),rgba(0,0,0,.15) 50%,rgba(0,0,0,.45))}
.nav{position:absolute;top:0;left:0;right:0;height:80px;z-index:2;display:flex;align-items:center;padding:0 40px}
.logo{font-family:"Caveat Brush",cursive;font-size:44px;color:var(--white)}
.nav-links{margin-left:auto;display:flex;gap:22px;align-items:center;font-size:13px;color:var(--white);font-weight:600}
.nav-phone{display:flex;align-items:center;gap:6px;margin-left:16px}
.hero-copy{position:absolute;z-index:2;left:0;right:0;top:255px;text-align:center;color:var(--white)}
.hero-copy h1{font-family:"Caveat Brush",cursive;font-size:56px;font-weight:400}
.hero-copy p{font-size:17px;font-weight:700;max-width:360px;margin:6px auto 22px;line-height:1.3}
.hero-copy .btn{margin:0 8px}

/* hours */
.hours{height:380px;background:var(--blue)}
.hours .title{color:var(--white);padding-top:86px}
.hours-row{display:flex;justify-content:center;gap:40px;margin-top:52px}
.hour-card{width:280px;height:110px;background:var(--blue-mid);border:1px solid var(--blue-soft);color:var(--white);text-align:center;padding-top:30px}
.hour-card h3{font-size:18px;font-weight:800}
.hour-card p{font-size:13px;margin-top:6px}

/* specials */
.specials{height:720px;background:linear-gradient(180deg,var(--blue-mist),#fff 40%,var(--blue-mist))}
.specials .title{color:var(--blue);padding-top:64px}
.specials .ph{left:540px;top:210px;width:660px;height:400px;background:linear-gradient(120deg,#3b2a1f,#8a6244 45%,#c9a27c 70%,#5a3d2a)}
.offer-card{position:absolute;left:100px;top:160px;width:440px;background:var(--white);box-shadow:0 6px 24px rgba(0,40,90,.18);padding:22px 26px;z-index:2}
.offer{position:relative;padding:14px 70px 14px 0;border-bottom:1px solid var(--blue-pale)}
.offer:last-child{border-bottom:none}
.offer h4{font-size:17px;font-weight:800;color:var(--red)}
.offer.blue h4{color:var(--blue)}
.offer.raised{background:var(--white);box-shadow:0 4px 16px rgba(0,40,90,.2);margin:6px -14px;padding:16px 80px 16px 14px}
.offer p{font-size:12px;line-height:1.45;color:var(--muted);margin-top:4px}
.price{position:absolute;right:6px;top:50%;transform:translateY(-50%);width:46px;height:46px;border-radius:50%;background:var(--red);color:#fff;font-weight:800;font-size:15px;display:flex;align-items:center;justify-content:center}
.offer.blue .price{background:var(--blue);right:18px}

/* private dining */
.private{height:420px;background:var(--blue-mist)}
.private .ph{left:0;top:0;width:600px;height:420px;background:linear-gradient(135deg,#6b4a34,#b58a63 40%,#e0c3a0 60%,#7a5a42)}
.private-panel{position:absolute;left:560px;top:70px;width:560px;background:var(--white);padding:30px 40px;text-align:center;box-shadow:0 6px 24px rgba(0,40,90,.12)}
.private-panel h2{font-family:"Caveat Brush",cursive;font-size:40px;color:var(--blue);font-weight:400}
.private-panel .lead{font-weight:800;font-size:14px;margin:6px 0 10px;color:var(--ink)}
.private-panel p{font-size:12.5px;color:var(--muted);line-height:1.5}
.private-panel .menu{color:var(--blue);font-weight:800;font-size:13px;margin-top:12px}
.private-panel .btn{margin-top:16px}

/* groups */
.groups{height:360px;background:var(--blue)}
.groups .title{color:var(--white);padding-top:62px}
.groups .sub{text-align:center;color:var(--blue-pale);font-size:13px;margin-top:6px}
.group-row{display:flex;justify-content:center;gap:70px;margin-top:40px}
.group-item{display:flex;align-items:center;gap:14px;color:var(--white);font-size:13px;width:200px;line-height:1.35}
.group-item .icon{width:70px;height:70px;flex:none;border-radius:50%;background:var(--blue-mid);border:2px solid var(--blue-soft);display:flex;align-items:center;justify-content:center}
.groups .cta{text-align:center;margin-top:40px}

/* cake */
.cake{height:580px;background:var(--white)}
.cake-copy{position:absolute;left:100px;top:80px;width:480px}
.cake-copy h2{font-family:"Caveat Brush",cursive;font-size:46px;color:var(--blue);font-weight:400;line-height:1}
.cake-copy .lead{font-weight:800;font-size:15px;margin-top:14px}
.cake-copy p{font-size:14px;margin-top:10px;line-height:1.45}
.cake-copy h5{font-size:14px;color:var(--blue);font-weight:800;margin-top:16px}
.cake-copy ul{list-style:none;margin-top:6px}
.cake-copy li{font-size:13.5px;padding:3px 0 3px 22px;position:relative}
.cake-copy li::before{content:"";position:absolute;left:0;top:7px;width:12px;height:12px;border-radius:50%;border:3px solid var(--blue)}
.cake-copy .note{color:var(--blue);font-size:13px;margin-top:14px}
.cake .ph{left:620px;top:80px;width:450px;height:400px;background:linear-gradient(160deg,#d9c9e0 0%,#b98a8a 40%,#7a5a4a 70%,#cbb6c8 100%)}

/* what's on */
.whatson{height:620px;background:var(--blue)}
.whatson .title{color:var(--white);padding-top:50px}
.event{position:absolute;background:var(--white);box-shadow:0 6px 20px rgba(0,0,0,.2)}
.event .img{position:absolute;background:linear-gradient(135deg,#6b5a48,#b89a7a 50%,#4a3c30)}
.event .info{position:absolute;font-size:11.5px;color:var(--muted);line-height:1.45}
.event .pp{font-size:17px;font-weight:800;color:var(--blue)}
.event .time{position:absolute;font-size:13px;color:var(--ink);font-weight:700}
.date{position:absolute;width:56px;height:64px;background:var(--red);color:#fff;text-align:center;font-weight:800;line-height:1.05;padding-top:10px}
.date b{display:block;font-size:22px}
.date span{font-size:12px}
.date.dark{background:#2b2b2b}
.sold{position:absolute;color:var(--red);font-weight:800;font-size:14px}
.event .btn{font-size:11px;padding:5px 16px}
.btn-yellow{background:var(--yellow);color:var(--ink)}

/* faq */
.faq{height:580px;background:linear-gradient(180deg,#fff,var(--blue-mist) 60%,#fff)}
.faq .title{color:var(--blue);padding-top:70px}
.faq-list{width:700px;margin:44px auto 0}
.q{display:flex;align-items:center;justify-content:space-between;background:var(--white);border:1px solid var(--blue-pale);padding:11px 14px;font-size:13px;font-weight:700;margin-bottom:12px}
.q .plus{width:20px;height:20px;border-radius:50%;border:1.5px solid var(--blue);color:var(--blue);display:flex;align-items:center;justify-content:center;font-size:14px;line-height:1}
.q.open{background:var(--blue);color:var(--white);border-color:var(--blue);margin-bottom:0}
.q.open .plus{border-color:#fff;color:#fff}
.answer{background:var(--white);border:1px solid var(--blue-pale);border-top:none;padding:14px;font-size:12.5px;line-height:1.55;color:var(--muted);margin-bottom:12px}
.faq .cta{text-align:center;margin-top:24px}

/* footer */
.site-footer{height:296px;background:var(--black);color:var(--white)}
.footer-logo{position:absolute;left:100px;top:70px;font-family:"Caveat Brush",cursive;font-size:56px}
.footer-col{position:absolute;top:50px}
.footer-col h6{font-size:15px;font-weight:800;color:var(--blue-soft);margin-bottom:12px}
.footer-col p{font-size:13px;line-height:1.5;color:#d7dde5}
.contact{left:330px;width:320px}
.contact .phone{position:absolute;left:230px;top:34px;font-size:13px;white-space:nowrap}
.contact .btn{position:absolute;left:230px;top:62px;border:1px solid #fff;color:#fff;font-size:12px;padding:5px 14px}
.feed{left:720px;width:380px}
.feed-row{display:flex;gap:10px}
.feed-row .ph{position:relative;width:120px;height:100px}
.socials{display:flex;gap:8px;justify-content:flex-end;margin-top:12px}
.socials i{width:26px;height:26px;border-radius:50%;background:var(--blue);display:block}
.copyright{position:absolute;left:0;right:0;bottom:0;height:60px;background:var(--blue);font-size:12px;color:#fff;padding:22px 100px}
</style>
</head>
<body>

<header class="hero">
  <div class="ph" role="img" aria-label="Photo of friends laughing and sharing plates at a dinner table"></div>
  <nav class="nav">
    <div class="logo">Marlo</div>
    <div class="nav-links">
      <span>Menus</span><span>Groups &amp; Functions</span><span>Gift Cards</span><span>Contact</span><span>FAQ</span>
      <span class="nav-phone"><svg width="14" height="14" viewBox="0 0 24 24" fill="#fff"><path d="M6.6 10.8a15 15 0 006.6 6.6l2.2-2.2a1 1 0 011-.25 11.4 11.4 0 003.6.57 1 1 0 011 1V20a1 1 0 01-1 1A17 17 0 013 4a1 1 0 011-1h3.5a1 1 0 011 1c0 1.25.2 2.45.57 3.6a1 1 0 01-.25 1z"/></svg>07 5550 1234</span>
      <a class="btn btn-solid">Book Now</a>
    </div>
  </nav>
  <div class="hero-copy">
    <h1>Marlo Kestra</h1>
    <p>Modern European styled restaurant overlooking the river at Kestraville</p>
    <a class="btn btn-solid">Book Now</a><a class="btn btn-outline">View Menus</a>
  </div>
</header>

<section class="hours">
  <h2 class="title">Open Hours</h2>
  <div class="hours-row">
    <div class="hour-card"><h3>~ Lunch ~</h3><p>Tues to Sun from 11.30am</p></div>
    <div class="hour-card"><h3>~ Dinner ~</h3><p>Tues to Sat from 5.30pm</p></div>
  </div>
</section>

<section class="specials">
  <h2 class="title">Specials / Offers</h2>
  <div class="ph" role="img" aria-label="Photo of a smiling waiter serving guests in the dining room"></div>
  <div class="offer-card">
    <div class="offer"><h4>Weekday Lunch</h4><p>Main Course<br>with glass of house wine, beer, or soft drink</p><span class="price">$35</span></div>
    <div class="offer blue raised"><h4>Saturday Lunch</h4><p>Bottomless Wine Lunch<br>3 Courses (last booking 2:15pm)</p><span class="price">$79</span></div>
    <div class="offer"><h4>Sunday Roast Lunch</h4><p>Roast Lunch<br>from noon until sold out. Our famous slow roast pork belly, with our chef's amazing crackling, cauliflower gratin, green beans, paris mash and apple sauce. Bookings advised.</p><span class="price">$42</span></div>
    <div class="offer"><h4>Wednesday</h4><p>Happy hour from 4pm followed by live music (5 - 8pm)</p></div>
  </div>
</section>

<section class="private">
  <div class="ph" role="img" aria-label="Photo of folded napkins and glassware set for a private dinner"></div>
  <div class="private-panel">
    <h2>Private Dining Room</h2>
    <p class="lead">Your perfect event overlooking the Kestra River</p>
    <p>Treat yourself and your guests to a more intimate event in our private dining room. With decorations inspired by an intimate French farmhouse style, our private room can cater for your special function from 12 to 38 guests.</p>
    <p class="menu">~ Set Menu ~</p>
    <p>Lunch from $60pp, Dinner from $75pp</p>
    <a class="btn btn-outline-blue">Details</a>
  </div>
</section>

<section class="groups">
  <h2 class="title">Groups + Functions</h2>
  <p class="sub">Host your celebration at Marlo</p>
  <div class="group-row">
    <div class="group-item"><span class="icon"><svg width="34" height="34" viewBox="0 0 24 24" fill="none" stroke="#fff" stroke-width="1.6"><circle cx="8" cy="8" r="3"/><circle cx="16" cy="8" r="3"/><path d="M2 20c0-3.3 2.7-6 6-6s6 2.7 6 6M10 20c0-3.3 2.7-6 6-6s6 2.7 6 6"/></svg></span>Groups of 12<br>or more</div>
    <div class="group-item"><span class="icon"><svg width="34" height="34" viewBox="0 0 24 24" fill="none" stroke="#fff" stroke-width="1.6"><rect x="3" y="9" width="18" height="3"/><path d="M5 12v8M19 12v8M8 5h8"/></svg></span>Large functions<br>up to 140 guests</div>
    <div class="group-item"><span class="icon"><svg width="34" height="34" viewBox="0 0 24 24" fill="none" stroke="#fff" stroke-width="1.6"><circle cx="12" cy="12" r="6"/><path d="M3 4v16M21 4v16"/></svg></span>Lunch or dinner<br>occasions</div>
  </div>
  <div class="cta"><a class="btn btn-outline">See More</a></div>
</section>

<section class="cake">
  <div class="cake-copy">
    <h2>Celebrating With A Cake</h2>
    <p class="lead">Create the perfect celebration cake</p>
    <p>Our pastry chef, Elise, can create the cake you're dreaming of.</p>
    <h5>Some suggestions:</h5>
    <ul>
      <li>White chocolate, blueberry and lemon cake</li>
      <li>Black forest (chocolate, cherries and cream)</li>
      <li>Dark chocolate mousse and honeycomb cake</li>
      <li>Carrot cake</li>
      <li>Fraisier (strawberry, mascarpone, sponge)</li>
      <li>Baked lemon cheese cake</li>
    </ul>
    <p class="note">Minimum charge $75 (up to 6 people) or $12 per person<br>*Take away – discount of 10% applies</p>
  </div>
  <div class="ph" role="img" aria-label="Photo of a decorated celebration cake with fruit and sparklers"></div>
</section>

<section class="whatson">
  <h2 class="title">What's On</h2>

  <div class="event" style="left:100px;top:130px;width:480px;height:190px">
    <div class="img" style="left:0;top:0;width:220px;height:190px" role="img" aria-label="Photo of guests at a winemaker dinner"></div>
    <div class="date" style="left:164px;top:90px"><b>10</b><span>Apr 23</span></div>
    <span class="sold" style="left:240px;top:14px">SOLD OUT</span>
    <div class="info" style="left:240px;top:36px"><span class="pp">$129</span> pp</div>
    <span class="time" style="left:345px;top:40px">6:30pm</span>
    <div class="info" style="left:345px;top:62px;width:125px">Harlow Wines – Amberly Valley<br>4 courses – 6 wines</div>
    <a class="btn btn-outline-blue" style="position:absolute;left:240px;top:140px">See More</a>
  </div>

  <div class="event" style="left:100px;top:345px;width:480px;height:190px">
    <div class="img" style="left:0;top:0;width:220px;height:190px" role="img" aria-label="Photo of a wine tasting evening"></div>
    <div class="date dark" style="left:164px;top:90px"><b>05</b><span>May 23</span></div>
    <div class="info" style="left:240px;top:30px"><span class="pp">$129</span> pp</div>
    <span class="time" style="left:345px;top:34px">6:30pm</span>
    <div class="info" style="left:345px;top:56px;width:125px">Harlow Wines – Amberly Valley<br>4 courses – 6 wines</div>
    <a class="btn btn-solid" style="position:absolute;left:240px;top:140px;font-size:11px;padding:5px 16px">See More</a>
  </div>

  <div class="event" style="left:610px;top:130px;width:490px;height:405px">
    <div class="img" style="left:0;top:0;width:490px;height:260px" role="img" aria-label="Photo of a full dining room at a wine event"></div>
    <div class="date dark" style="left:420px;top:220px"><b>28</b><span>Apr 23</span></div>
    <div class="info" style="left:24px;top:290px"><span class="pp">$129</span> pp</div>
    <span class="time" style="left:150px;top:294px">6:30pm</span>
    <div class="info" style="left:150px;top:316px">Harlow Wines – Amberly Valley, 4 courses – 6 wines</div>
    <a class="btn btn-outline-blue" style="position:absolute;left:24px;top:355px">See More</a>
    <a class="btn btn-yellow" style="position:absolute;left:150px;top:355px">Last Bookings</a>
  </div>
</section>

<section class="faq">
  <h2 class="title">Frequently Asked Questions</h2>
  <div class="faq-list">
    <div class="q">What is Lorem Ipsum?<span class="plus">+</span></div>
    <div class="q">Duis tristique leo at pretium malesuada?<span class="plus">+</span></div>
    <div class="q open">Quisque non nisi dapibus, luctus tempor mauris?<span class="plus">−</span></div>
    <div class="answer">Lorem Ipsum is simply dummy text of the printing and typesetting industry. Lorem Ipsum has been the industry's standard dummy text ever since the 1500s, when an unknown printer took a galley of type and scrambled it to make a type specimen book. It has survived not only five centuries, but also the leap into electronic typesetting, remaining essentially unchanged.</div>
    <div class="q">Aenean nec ligula eget justo malesuada congue?<span class="plus">+</span></div>
  </div>
  <div class="cta"><a class="btn btn-outline-blue">View All</a></div>
</section>

<footer class="site-footer">
  <div class="footer-logo">Marlo</div>
  <div class="footer-col contact">
    <h6>Contact Us</h6>
    <p>Marlo Kestra<br>18 Riverbend Parade<br>Kestraville QLD 4999</p>
    <span class="phone">Tel: 07 5550 1234</span>
    <a class="btn">Book Now</a>
  </div>
  <div class="footer-col feed">
    <h6>Photo Feed</h6>
    <div class="feed-row">
      <div class="ph" style="background:linear-gradient(135deg,#5a4434,#a98465)" role="img" aria-label="Photo of a plated dish"></div>
      <div class="ph" style="background:linear-gradient(135deg,#2f4c6e,#7ba0c4)" role="img" aria-label="Photo of the river view from the terrace"></div>
      <div class="ph" style="background:linear-gradient(135deg,#6e3a34,#c48a6a)" role="img" aria-label="Photo of wine glasses at the bar"></div>
    </div>
    <div class="socials"><i></i><i></i></div>
  </div>
  <div class="copyright">© 2023 Marlo Kestra . All Right Reserved.</div>
</footer>

</body>
</html>
```